Supplement Rebranding Bottle Design

READ WORD DOCUMENT ATTACHED.
We want to rebrand our current health supplements (see below). We do want it to be modern, vibrant and appealing. Very upscale and elegant as it targets primarily women.
Bottle size: see pictures for bottle size, along with sample bottles that we like; we’re open to any bottle similar to the ones attached.
Current bottles: So ideally, we’d keep the core color on each bottle with a new branding/bottle design. But we're open to your suggestion.

Target Market(s)

mostly women but shouldn't be overly feminine

Requirements
Must have
• see bottle sizes attached

```html
<!DOCTYPE html>
<html lang="en">
<head>
<meta charset="UTF-8">
<title>Belly Ease Formula – Supplement Label</title>
<link href="https://fonts.googleapis.com/css2?family=Outfit:wght@400;500;800&family=Oswald:wght@500&display=swap" rel="stylesheet">
<style>
  :root {
    --backdrop: #f2f2f2;
    --label-white: #f7f7f7;
    --label-red: #dd0a0d;
    --ink-dark: #2b2b2b;
    --ink-mid: #3a3a3a;
    --ink-light: #ffffff;
    --ink-soft: #f4c9c9;
  }
  html, body {
    margin: 0;
    padding: 0;
    width: 1200px;
    height: 900px;
    overflow: hidden;
    background: var(--backdrop);
    font-family: "Outfit", sans-serif;
  }
  .canvas {
    position: relative;
    width: 1200px;
    height: 900px;
  }
  .label {
    position: absolute;
    left: 370px;
    top: 90px;
    width: 460px;
    height: 720px;
    border-radius: 14px;
    overflow: hidden;
    box-shadow: 0 6px 24px rgba(0, 0, 0, 0.08);
  }
  .label-top {
    position: relative;
    height: 374px;
    background: var(--label-white);
  }
  .label-bottom {
    position: relative;
    height: 346px;
    background: var(--label-red);
  }
  .brand-name {
    position: absolute;
    left: 50px;
    top: 160px;
    margin: 0;
    font-size: 24px;
    font-weight: 800;
    line-height: 1;
    letter-spacing: -0.3px;
    white-space: nowrap;
    color: var(--ink-dark);
  }
  .product-type {
    position: absolute;
    left: 50px;
    top: 334px;
    margin: 0;
    font-size: 14px;
    font-weight: 400;
    line-height: 1;
    letter-spacing: 4.2px;
    white-space: nowrap;
    color: var(--ink-mid);
  }
  .product-claim {
    position: absolute;
    left: 58px;
    top: 222px;
    margin: 0;
    font-size: 15px;
    font-weight: 500;
    line-height: 1.15;
    color: var(--ink-light);
  }
  .capsule-count {
    position: absolute;
    right: 42px;
    top: 220px;
    display: flex;
    align-items: center;
    gap: 6px;
    color: var(--ink-light);
  }
  .capsule-count .number {
    font-family: "Oswald", sans-serif;
    font-weight: 500;
    font-size: 38px;
    line-height: 1;
  }
  .capsule-count .unit {
    font-size: 8.5px;
    line-height: 1.15;
    letter-spacing: 0.3px;
    color: var(--ink-soft);
  }
</style>
</head>
<body>
  <main class="canvas">
    <section class="label">
      <div class="label-top">
        <p class="brand-name">Belly Ease Formula</p>
        <p class="product-type">DIETARY SUPPLEMENT</p>
      </div>
      <div class="label-bottom">
        <p class="product-claim">Oxygenating Colon<br>Cleanse</p>
        <div class="capsule-count">
          <span class="number">90</span>
          <span class="unit">VEGETABLE<br>CAPSULES</span>
        </div>
      </div>
    </section>
  </main>
</body>
</html>
```